Require an amazing and engaging Home Page redesign! For New Startup!

We require a new design for our home page of www.quonmart.com.au.

We want this to be in a similar theme to the current site, all other pages to remain unchanged however our marketing team have advised that the current home page (initial banner) is not engaging or "hooking" potential leads. I have attached "CRO Recommendations" from our marketing team as an idea to the issues with the Quonmart site.
At the moment we would only like the issues on home page reviewed (Pages: 4 to 10).

I have attached an example from our marketing team as to an idea of how the front home page needs to look.

As an idea of what our competition is doing well please view zestmotors.com.au, drivepeak.com.au (great engagement on home page top banner).

Quonmart is a brand new concept for Australian new car buyers. Quonmart allows a customer buying a new car to receive best price offer for their new car needs and finance requirements all on a sophisticated online dashboard. The dashboard even allows the customer to interact directly with the dealerships to negotiate the price online! (never offered before).

I've provided new logo, brand guidelines for colour and font scheme.

View the website to get an idea of what Quonmart is all about and let's see what we can come up with.

Thanks.

Target Market(s)

Females, age between 21-35

Industry/Entity Type

Automotive

Number of Pages Required

1 page

Requirements
Must have
• Engaging initial banner. We want to see the banner as mocked up and provided but also maybe provide an option showing a large graphic as the banner that incorporates this "hook" for engagement.
• Minimal menu (no Need Help or Newsletter buttons) with new logo on left.
• As per design mockup. Looking for engaging banner.
• Why it Works benefits section - 3 to 4 key benefits
• Customer satisfaction/testimonial area
Nice to have
• As Seen On banner or icon somewhere - maybe near or under the "Get Offers' buttons? As we have been featured in the COASTAL POST

```html
<!DOCTYPE html>
<html lang="en">
<head>
<meta charset="utf-8">
<title>Quonmart – Experience the Revolution in Car Buying</title>
<link href="https://fonts.googleapis.com/css2?family=Montserrat:wght@300;400;500;600;700&family=Kalam:wght@700&family=Roboto+Condensed:wght@400;700&display=swap" rel="stylesheet">
<style>
  :root{
    --blue:#1d5a82;
    --blue-dark:#1a4f74;
    --gold:#e0a526;
    --ink:#2c2c2c;
    --white:#ffffff;
    --grey:#f1f1f1;
    --teal:#2f6a7a;
  }
  *{margin:0;padding:0;box-sizing:border-box}
  html,body{width:1200px;height:1200px;overflow:hidden;background:var(--white)}
  body{position:relative;font-family:"Montserrat",sans-serif;color:var(--ink)}

  /* Header */
  .site-header{position:absolute;left:0;top:0;width:1200px;height:104px;background:var(--white)}
  .brand{position:absolute;left:256px;top:30px;display:flex;align-items:center;gap:12px}
  .brand-dot{width:44px;height:44px;border-radius:50%;border:4px solid var(--gold)}
  .brand-name{font-weight:700;font-size:19px;color:var(--blue);letter-spacing:.3px}
  .main-nav{position:absolute;top:44px;left:440px;font-size:13px;color:var(--blue)}
  .main-nav a{position:absolute;white-space:nowrap;color:inherit;text-decoration:none}
  .phone{position:absolute;left:861px;top:42px;display:flex;align-items:center;gap:6px;color:var(--gold);font-size:14.5px;font-weight:500}

  /* Hero */
  .hero{position:absolute;left:0;top:104px;width:1200px;height:400px;
    background:radial-gradient(ellipse at 75% 70%,#22262c 0%,#0d0f12 45%,#050607 100%)}
  .hero-sky{position:absolute;inset:0;background:linear-gradient(180deg,rgba(60,70,85,.35) 0%,rgba(0,0,0,0) 60%)}
  .hero-title{position:absolute;top:92px;width:100%;text-align:center;color:var(--white);font-weight:600;font-size:29px;letter-spacing:.2px}
  .hero-tagline{position:absolute;top:146px;width:100%;text-align:center;color:var(--gold);font-family:"Kalam",cursive;font-size:24px}
  .hero-sub{position:absolute;top:184px;width:100%;text-align:center;color:var(--white);font-weight:300;font-size:22px}
  .btn-apply{position:absolute;left:499px;top:254px;width:201px;height:48px;border:1.5px solid var(--white);border-radius:3px;
    display:flex;align-items:center;justify-content:center;color:var(--gold);font-weight:700;font-size:18px;font-variant:small-caps;letter-spacing:.5px;background:rgba(0,0,0,.4)}

  /* Steps */
  .steps-title{position:absolute;top:549px;width:100%;text-align:center;color:var(--blue);font-weight:700;font-size:19px}
  .steps-sub{position:absolute;top:577px;width:100%;text-align:center;color:var(--gold);font-weight:500;font-size:11px}
  .step{position:absolute;top:612px;width:200px;text-align:center}
  .step svg{display:block;margin:0 auto}
  .step-caption{margin-top:14px;font-size:12px;line-height:14.5px;color:var(--ink)}

  /* Plans */
  .plans{position:absolute;left:0;top:862px;width:1200px;height:338px;
    background:radial-gradient(circle at 58% 40%,#143a55 0%,#0b1a24 30%,#06080b 70%),#06080b}
  .plan{position:absolute;top:48px;width:173px;height:250px;background:var(--white);border:1px solid #d8d8d8}
  .price{position:absolute;left:-21px;top:-10px;width:42px;height:42px;border-radius:50%;background:var(--white);border:2px solid var(--blue);
    display:flex;align-items:center;justify-content:center;font-size:14px;color:var(--ink)}
  .plan-title{position:absolute;top:12px;left:14px;right:6px;text-align:center;color:var(--blue);font-weight:600;font-size:11px;line-height:13.5px}
  .features{position:absolute;top:56px;left:14px;right:10px;list-style:none}
  .features li{position:relative;padding-left:16px;font-size:8.5px;line-height:10.5px;margin-bottom:11px;color:var(--ink)}
  .features li svg{position:absolute;left:0;top:0}
  .select{position:absolute;left:16px;width:140px;height:17px;background:var(--grey);font-family:"Roboto Condensed",sans-serif;font-size:8.5px;color:var(--blue);
    display:flex;align-items:center;justify-content:space-between;padding:0 8px}
  .select .caret{width:0;height:0;border-left:4px solid transparent;border-right:4px solid transparent;border-top:6px solid var(--gold)}
  .select.amount{color:var(--gold)}
  .btn-offers{position:absolute;left:17px;top:212px;width:138px;height:28px;background:var(--blue-dark);border-radius:3px;color:var(--white);
    font-family:"Roboto Condensed",sans-serif;font-size:12.5px;display:flex;align-items:center;justify-content:center}
</style>
</head>
<body>

<header class="site-header">
  <div class="brand"><span class="brand-dot"></span><span class="brand-name">QUONMART</span></div>
  <nav class="main-nav">
    <a style="left:0">How it works</a>
    <a style="left:106px">Pricing</a>
    <a style="left:174px">FAQ</a>
    <a style="left:224px">Apply</a>
    <a style="left:284px">Login</a>
  </nav>
  <div class="phone">
    <svg width="20" height="20" viewBox="0 0 20 20"><circle cx="10" cy="10" r="9" fill="none" stroke="#e0a526" stroke-width="1.5"/><path d="M7 5.5l1.6 2.3-1 1.1c.6 1.3 1.6 2.3 2.9 2.9l1.1-1 2.3 1.6-.8 1.6c-3.6-.3-6.6-3.3-6.9-6.9z" fill="#e0a526"/></svg>
    1300 482 916
  </div>
</header>

<section class="hero">
  <div class="hero-sky" role="img" aria-label="Photo of a classic convertible sports car under a dark cloudy night sky"></div>
  <h1 class="hero-title">EXPERIENCE THE REVOLUTION IN CAR BUYING</h1>
  <p class="hero-tagline">Fleet car prices without the costs!</p>
  <p class="hero-sub">Australia's Best New Car &amp; Loan deals</p>
  <a class="btn-apply">Apply Now</a>
</section>

<h2 class="steps-title">A REVOLUTION IN CAR BUYING HAS ARRIVED.</h2>
<p class="steps-sub">Get car dealera and lenders to bid for YOUR business today.</p>

<svg width="0" height="0" style="position:absolute">
  <defs>
    <linearGradient id="ring" x1="0" y1="0" x2="0" y2="1">
      <stop offset="0" stop-color="#d6a62c"/>
      <stop offset="1" stop-color="#2b5f78"/>
    </linearGradient>
  </defs>
</svg>

<div class="step" style="left:251px">
  <svg width="200" height="170" viewBox="0 0 200 170">
    <circle cx="100" cy="80" r="78" fill="none" stroke="url(#ring)" stroke-width="3.5"/>
    <circle cx="45" cy="24" r="24" fill="#fff" stroke="#e0a526" stroke-width="1.5"/>
    <text x="45" y="31" text-anchor="middle" font-family="Montserrat,sans-serif" font-weight="600" font-size="17" fill="#2c2c2c">1</text>
    <path d="M78 80h8v32h-8zM90 80l12-18c2-4 3-10 4-14 5 0 9 4 8 10l-3 12h14c5 0 8 4 7 8l-4 22c-1 4-4 7-8 7H90z" fill="#333"/>
  </svg>
  <p class="step-caption">Submit your car or<br>finance needs</p>
</div>

<div class="step" style="left:500px">
  <svg width="200" height="170" viewBox="0 0 200 170">
    <circle cx="100" cy="80" r="78" fill="none" stroke="url(#ring)" stroke-width="3.5"/>
    <circle cx="45" cy="24" r="24" fill="#fff" stroke="#e0a526" stroke-width="1.5"/>
    <text x="45" y="31" text-anchor="middle" font-family="Montserrat,sans-serif" font-weight="600" font-size="17" fill="#2c2c2c">2</text>
    <g transform="rotate(-45 88 68)"><rect x="72" y="50" width="34" height="22" rx="2" fill="#333"/><rect x="68" y="54" width="6" height="14" fill="#333"/><rect x="104" y="54" width="6" height="14" fill="#333"/></g>
    <path d="M94 72l4-4 34 36-4 4z" fill="#333"/>
  </svg>
  <p class="step-caption">Dealership and lenders<br>submit their best offers</p>
</div>

<div class="step" style="left:749px">
  <svg width="200" height="170" viewBox="0 0 200 170">
    <circle cx="100" cy="80" r="78" fill="none" stroke="url(#ring)" stroke-width="3.5"/>
    <circle cx="45" cy="24" r="24" fill="#fff" stroke="#e0a526" stroke-width="1.5"/>
    <text x="45" y="31" text-anchor="middle" font-family="Montserrat,sans-serif" font-weight="600" font-size="17" fill="#2c2c2c">3</text>
    <path d="M92 52c0-4 7-4 7 0v22c4-2 8 0 8 2 4-1 8 1 8 3 4-1 7 1 7 4v16c0 8-4 12-6 16H97l-14-24c-2-4 3-7 6-4l3 4z" fill="#333"/>
  </svg>
  <p class="step-caption">You choose the best deal online<br>and exchange contact details.<br>It's that easy!</p>
</div>

<section class="plans" role="img" aria-label="Close-up photo of a glowing car speedometer dial">
  <div class="plan" style="left:272px">
    <div class="price">$47</div>
    <h3 class="plan-title">I just need the best<br>dealson a new car.</h3>
    <ul class="features">
      <li><svg width="12" height="10" viewBox="0 0 12 10"><path d="M1 5l3 3 7-7" fill="none" stroke="#e0a526" stroke-width="2.2"/></svg>3 dealership best price car quotes</li>
    </ul>
    <div class="select" style="top:164px">Car Model<span class="caret"></span></div>
    <div class="select" style="top:188px">Car Make<span class="caret"></span></div>
    <div class="btn-offers">Get Offers</div>
  </div>

  <div class="plan" style="left:514px">
    <div class="price">$47</div>
    <h3 class="plan-title">I need the best deals<br>on a new car and finance</h3>
    <ul class="features">
      <li><svg width="12" height="10" viewBox="0 0 12 10"><path d="M1 5l3 3 7-7" fill="none" stroke="#e0a526" stroke-width="2.2"/></svg>3dealership best price<br>car quotes</li>
      <li><svg width="12" height="10" viewBox="0 0 12 10"><path d="M1 5l3 3 7-7" fill="none" stroke="#e0a526" stroke-width="2.2"/></svg>3car financequotes<br>from our broker panel</li>
    </ul>
    <div class="select" style="top:164px">Car Model<span class="caret"></span></div>
    <div class="select" style="top:188px">Car Make<span class="caret"></span></div>
    <div class="btn-offers">Get Offers</div>
  </div>

  <div class="plan" style="left:776px">
    <div class="price">$7</div>
    <h3 class="plan-title">I just want the best deal<br>on my car finance.</h3>
    <ul class="features">
      <li><svg width="12" height="10" viewBox="0 0 12 10"><path d="M1 5l3 3 7-7" fill="none" stroke="#e0a526" stroke-width="2.2"/></svg>Perfect for new or used<br>cars</li>
      <li><svg width="12" height="10" viewBox="0 0 12 10"><path d="M1 5l3 3 7-7" fill="none" stroke="#e0a526" stroke-width="2.2"/></svg>Receive up to 3 live loan<br>quates</li>
      <li><svg width="12" height="10" viewBox="0 0 12 10"><path d="M1 5l3 3 7-7" fill="none" stroke="#e0a526" stroke-width="2.2"/></svg>Guaranteed to best<br>dealership finance</li>
      <li><svg width="12" height="10" viewBox="0 0 12 10"><path d="M1 5l3 3 7-7" fill="none" stroke="#e0a526" stroke-width="2.2"/></svg>Quotes from our<br>award-winning broker<br>panel</li>
    </ul>
    <div class="select amount" style="top:182px;justify-content:flex-start;gap:8px">$ <span>Estimated Loan Amount...</span></div>
    <div class="btn-offers">Get Offers</div>
  </div>
</section>

</body>
</html>
```